Business Card Design

I'm a young beekeeper (22 years old) just starting out. I own and run 80 hives and would like to eventually build up to 1000. My aim is to run it in tandem with our family farm that is currently running sheep and beef. Unlike a number of honey companies on the East Coast (or the North Island, NZ) I am local and will expand onto the lease blocks that our family is also leasing. I want a simple plain logo/photo. The designer may wish to use one of the photos as a background outline or however they chose. The mountain is Aorangi and our farm borders one side of it.

Target Market(s)

From local land owners to wholesale honey buyers

Industry/Entity Type

Farm

Contact Information for Business Card

Pekeriu Honey
Manager Owner Manaia Brooks
email pekeriuhoney@tuimailbox.co.nz
mobile 0217394461

Requirements
Must have
• The details submitted. The brand Pekeriu Honey to be the main feature. The other details can be smaller.
Should not have
• Must not include a picture of a bee or hive. Use a modern font. Don't use koru but may incorporate poutama.

```html
<!DOCTYPE html>
<html lang="en">
<head>
<meta charset="utf-8">
<title>Pekeriu Honey – Business Card</title>
<link rel="stylesheet" href="https://fonts.googleapis.com/css2?family=Cabin:wght@500;600;700&family=Great+Vibes&display=swap">
<style>
  :root {
    --frame-yellow: #f3d400;
    --sky-light: #f4f8fb;
    --sky-blue: #c9dcec;
    --mountain-haze: #8c9aa8;
    --mountain-deep: #5e6c78;
    --ground-light: #e6e2d6;
    --ground-warm: #cfc8b4;
    --ink-black: #111111;
    --accent-red: #c8201e;
    --ink-navy: #1d2247;
  }
  html, body {
    margin: 0;
    padding: 0;
    width: 1200px;
    height: 807px;
    overflow: hidden;
    background: #ffffff;
  }
  .business-card {
    position: relative;
    width: 1200px;
    height: 807px;
    box-sizing: border-box;
    border: 10px solid var(--frame-yellow);
    overflow: hidden;
    font-family: "Cabin", "Trebuchet MS", sans-serif;
  }
  .landscape-backdrop {
    position: absolute;
    inset: 0;
    background:
      linear-gradient(180deg,
        var(--sky-light) 0%,
        var(--sky-blue) 24%,
        var(--mountain-haze) 38%,
        var(--mountain-deep) 52%,
        var(--mountain-haze) 62%,
        var(--ground-light) 74%,
        var(--ground-warm) 100%);
    opacity: 0.85;
  }
  .brand-name {
    position: absolute;
    left: 128px;
    top: 218px;
    margin: 0;
    font-family: "Great Vibes", cursive;
    font-weight: 400;
    font-size: 132px;
    line-height: 1;
    color: var(--ink-black);
    white-space: nowrap;
  }
  .role-title {
    position: absolute;
    right: 88px;
    top: 356px;
    margin: 0;
    font-weight: 700;
    font-size: 58px;
    line-height: 1;
    color: var(--accent-red);
  }
  .owner-name {
    position: absolute;
    left: 200px;
    top: 452px;
    margin: 0;
    font-weight: 500;
    font-size: 72px;
    line-height: 1;
    color: var(--ink-navy);
    white-space: nowrap;
  }
  .contact-line {
    position: absolute;
    left: 0;
    right: 0;
    margin: 0;
    text-align: center;
    font-weight: 600;
    line-height: 1;
    color: var(--ink-black);
    white-space: nowrap;
  }
  .contact-email {
    top: 640px;
    font-size: 48px;
  }
  .contact-mobile {
    top: 712px;
    font-size: 48px;
  }
</style>
</head>
<body>
  <div class="business-card">
    <div class="landscape-backdrop" role="img" aria-label="Photograph of a mountain peak under a pale sky with sunlit grassy farmland in the foreground"></div>
    <h1 class="brand-name">Pekeriu Honey</h1>
    <p class="role-title">Manager</p>
    <p class="owner-name">Owner Manaia Brooks</p>
    <p class="contact-line contact-email">E-mail : pekeriuhoney@tuimailbox.co.nz</p>
    <p class="contact-line contact-mobile">Mob. : 0217394461</p>
  </div>
</body>
</html>
```